Business Card Velostra - Accounting firm

Hi my friend.
I'm coming back to you to see if it would be possible for you to make a modern and minimalist business card design.
In shades of blue like the great logo you offered me.
The ideal is a modern and aesthetic business card.
The goal is to give a professional effect to the first exchanges.
Renewal and innovation in the accounting world !!
I thank you !!
Good evening to you

Target Market(s)

Young, dynamic and sensitive to marketing

Industry/Entity Type

Finance And Accounting

Contact Information for Business Card

Company logo and name. Last name, First name, Phone number, email address, company address, website.

Font styles to use
Sans Serif

Requirements
Must have
• The ideal is a modern and aesthetic business card.

Mentions to include: Company logo and name. Last name, First name, Phone number, email address, company address, website.
Nice to have
• The goal is to give a professional effect to the first exchanges.
Should not have
• Simplistic or childish design

```html
<!DOCTYPE html>
<html lang="en">
<head>
<meta charset="utf-8">
<title>Velostra – Business Card</title>
<link rel="stylesheet" href="https://fonts.googleapis.com/css2?family=Poppins:wght@400;500;600;700&display=swap">
<style>
  :root{
    --backdrop:#2a2a2c;
    --card-white:#ffffff;
    --navy:#04255f;
    --teal:#3fd2c0;
    --sky:#1a8fd0;
    --ink-light:#ffffff;
  }
  *{box-sizing:border-box;margin:0;padding:0}
  html,body{width:1200px;height:880px;overflow:hidden}
  body{
    background:var(--backdrop);
    font-family:"Poppins",sans-serif;
    position:relative;
  }
  .card{
    position:absolute;
    width:540px;height:310px;
    background:var(--card-white);
    border-radius:18px;
    overflow:hidden;
    top:285px;
  }
  .card--front{left:40px}
  .card--back{left:620px}

  .brand{
    display:flex;align-items:center;gap:14px;
    color:var(--navy);
    font-weight:600;
    letter-spacing:-1px;
  }
  .brand__dot{
    border-radius:50%;
    background:var(--teal);
    flex:none;
  }
  .card--front .brand{
    position:absolute;left:50%;top:50%;
    transform:translate(-50%,-50%);
    font-size:62px;
  }
  .card--front .brand__dot{width:46px;height:46px}

  .card--back .brand{
    position:absolute;left:34px;top:50%;
    transform:translateY(-50%);
    font-size:38px;
    gap:10px;
  }
  .card--back .brand__dot{width:30px;height:30px}

  .back-shape{position:absolute;inset:0;width:540px;height:310px}

  .details{
    position:absolute;right:30px;top:34px;
    text-align:right;color:var(--ink-light);
  }
  .details__name{font-size:19px;font-weight:700;letter-spacing:.3px;line-height:1.1}
  .details__role{font-size:13px;color:var(--teal);font-weight:500;margin-bottom:26px}
  .details__address{font-size:12px;line-height:1.5;margin-bottom:12px}
  .contact-list{list-style:none}
  .contact-list li{
    display:flex;justify-content:flex-end;align-items:center;gap:8px;
    font-size:12px;line-height:1.8;
  }
  .contact-list svg{width:14px;height:14px;flex:none}
</style>
</head>
<body>

  <section class="card card--front" aria-label="Business card front">
    <div class="brand"><span class="brand__dot"></span>velostra</div>
  </section>

  <section class="card card--back" aria-label="Business card back">
    <svg class="back-shape" viewBox="0 0 540 310" aria-hidden="true">
      <defs>
        <linearGradient id="arcGrad" x1="0" y1="0" x2="0" y2="1">
          <stop offset="0" stop-color="var(--teal)"/>
          <stop offset="1" stop-color="var(--sky)"/>
        </linearGradient>
      </defs>
      <path d="M200 0 C330 30 370 200 300 310 L540 310 L540 0 Z" fill="var(--navy)"/>
      <path d="M255 50 C335 110 345 230 280 310 L300 310 C362 225 350 110 255 50 Z" fill="url(#arcGrad)"/>
      <path d="M262 55 C340 115 352 230 292 310" fill="none" stroke="#fff" stroke-width="3"/>
    </svg>

    <div class="brand"><span class="brand__dot"></span>velostra</div>

    <div class="details">
      <p class="details__name">JULIEN MARLOWE</p>
      <p class="details__role">Managing Director</p>
      <p class="details__address">Po Box 5120<br>8 Harbor Lane, Leeds, UK</p>
      <ul class="contact-list">
        <li>+44 555 014 2290
          <svg viewBox="0 0 16 16"><circle cx="8" cy="8" r="7" fill="none" stroke="var(--teal)" stroke-width="1.4"/><path d="M5.5 4.5l1.5 1.5-1 1a5 5 0 0 0 3 3l1-1 1.5 1.5-1 1c-3 0-6-3-6-6z" fill="var(--teal)"/></svg></li>
        <li>+44 555 014 2291
          <svg viewBox="0 0 16 16"><circle cx="8" cy="8" r="7" fill="none" stroke="var(--teal)" stroke-width="1.4"/><rect x="5.5" y="4" width="5" height="8" rx="1" fill="none" stroke="var(--teal)" stroke-width="1.2"/></svg></li>
        <li>hello@velostra-mail.com
          <svg viewBox="0 0 16 16"><circle cx="8" cy="8" r="7" fill="none" stroke="var(--teal)" stroke-width="1.4"/><rect x="4.5" y="5.5" width="7" height="5" fill="none" stroke="var(--teal)" stroke-width="1.1"/><path d="M4.5 5.5L8 8.5l3.5-3" fill="none" stroke="var(--teal)" stroke-width="1.1"/></svg></li>
        <li>www.velostra-web.com
          <svg viewBox="0 0 16 16"><circle cx="8" cy="8" r="7" fill="none" stroke="var(--teal)" stroke-width="1.4"/><circle cx="8" cy="8" r="3.5" fill="none" stroke="var(--teal)" stroke-width="1.1"/><path d="M4.5 8h7M8 4.5v7" stroke="var(--teal)" stroke-width="1"/></svg></li>
      </ul>
    </div>
  </section>

</body>
</html>
```